Velora Studio business site requires luxurious wix template design

I need a wix web template design that will deliver a consistent look and feel across mobile and computer access. Designs should follow the boudoir theme, be classy, and luxurious looking. Gold or silver inlay, velvet feel.
The majority of my clients will be women from the age of 22-40, and will be interested in boosting their self-esteem, feeling feminine, romance etc. They may want a shoot to celebrate a pending wedding, or a fitness achievement.

Target Market(s)

Females between 22-40 years of age

Logo Text

Velora Studio Canada (or Velora Studio)

Font styles to use
Decorative
Script

Colors

Designer to choose colors to be used in the design.

Requirements
Must have
• Site will have booking component for appointments, merchandise may be made available (photos, books)

```html
<!DOCTYPE html>
<html lang="en">
<head>
<meta charset="utf-8">
<title>Velora Studio</title>
<link rel="stylesheet" href="https://fonts.googleapis.com/css2?family=Great+Vibes&family=Lato:ital,wght@0,400;0,700;1,400&display=swap">
<style>
:root{
  --ink:#1a1a1a;
  --text:#333333;
  --muted:#555555;
  --panel:#f5f5f5;
  --page:#ffffff;
  --line:#444444;
  --black:#000000;
  --gold:#b8965a;
  --gold-soft:rgba(184,150,90,.55);
  --silver:#d9d9dc;
}
*{box-sizing:border-box;margin:0;padding:0}
html,body{width:1200px;height:3734px;overflow:hidden;background:var(--page)}
body{position:relative;font-family:'Lato',Arial,sans-serif;color:var(--text)}
.abs{position:absolute}
.script{font-family:'Great Vibes',cursive;font-weight:400;color:var(--ink)}

/* header */
.menu-toggle{left:82px;top:24px;font-size:12px;color:var(--ink);letter-spacing:.5px;line-height:14px}
.menu-toggle span{display:block;height:3px;background:var(--ink);margin-top:4px}
.menu-toggle .l1{width:22px}.menu-toggle .l2{width:16px}
.brand{left:0;width:1200px;top:24px;text-align:center;font-size:26px;line-height:34px;color:var(--ink);letter-spacing:1px}
.brand::before{content:"";display:inline-block;width:12px;height:12px;border:2px solid var(--gold);border-radius:50%;margin-right:8px;vertical-align:middle}
.book-link{right:78px;top:32px;font-size:13px;color:var(--ink);text-decoration:underline}
.main-nav{left:0;width:1200px;top:95px;display:flex;justify-content:center;gap:34px;font-size:12px;letter-spacing:1px;color:var(--muted)}
.main-nav .active{color:var(--ink);font-weight:700;border-bottom:2px solid var(--gold);padding-bottom:4px}

/* photo areas */
.photo{box-shadow:inset 0 0 0 1px var(--gold-soft)}
.hero-photo{left:82px;top:120px;width:1040px;height:552px;
  background:
    radial-gradient(ellipse 30% 45% at 20% 45%,#5a3e38 0%,rgba(90,62,56,0) 70%),
    radial-gradient(ellipse 35% 30% at 55% 40%,#b9d0e2 0%,rgba(185,208,226,0) 75%),
    radial-gradient(ellipse 40% 35% at 60% 80%,#e7cfc4 0%,rgba(231,207,196,0) 75%),
    linear-gradient(110deg,#d7d4da 0%,#ecebee 40%,#e3e6ea 70%,#f7f7f7 100%)}
.hero-pre{left:732px;top:322px;font-size:19px;line-height:22px;letter-spacing:1.5px;color:var(--ink)}
.hero-big{left:640px;top:338px;font-family:'Great Vibes',cursive;font-size:108px;line-height:110px;color:var(--ink)}
.hero-post{left:728px;top:422px;font-size:19px;line-height:22px;letter-spacing:5px;color:var(--ink)}

/* about */
.about-panel{left:82px;top:672px;width:1040px;height:420px;background:var(--panel)}
.section-title{left:0;width:1200px;text-align:center;font-size:44px;line-height:56px}
.about-copy{left:245px;width:710px;text-align:center;font-size:13px;line-height:19px;color:var(--text)}
.btn{display:flex;align-items:center;justify-content:center;background:var(--black);color:#fff;font-size:13px;letter-spacing:1px;box-shadow:inset 0 0 0 1px var(--gold-soft)}

/* services */
.service{width:308px;height:308px;border-radius:50%;display:flex;align-items:center;justify-content:center;box-shadow:0 0 0 1px var(--gold-soft)}
.service .label{font-family:'Great Vibes',cursive;font-size:40px;color:#fff;border-top:1px solid var(--silver);border-bottom:1px solid var(--silver);width:192px;text-align:center;line-height:62px}
.svc-wedding{left:115px;top:1245px;background:
  radial-gradient(circle at 50% 70%,#ecdcd0 0%,rgba(236,220,208,0) 40%),
  radial-gradient(circle at 80% 40%,#8d7a66 0%,rgba(141,122,102,0) 35%),
  linear-gradient(160deg,#e8e4e0,#c9beb6)}
.svc-boudoir{left:447px;top:1245px;background:
  radial-gradient(circle at 40% 25%,#c9a995 0%,rgba(201,169,149,0) 30%),
  radial-gradient(circle at 65% 65%,#6e2f33 0%,rgba(110,47,51,0) 50%),
  linear-gradient(160deg,#d8d6d6,#4a3a3c)}
.svc-outdoors{left:777px;top:1245px;background:
  radial-gradient(circle at 45% 30%,#7a2f22 0%,rgba(122,47,34,0) 30%),
  radial-gradient(circle at 55% 85%,#e3aa22 0%,rgba(227,170,34,0) 40%),
  linear-gradient(160deg,#8ba69a,#a68b58 60%,#806f45)}

/* gallery */
.gallery-panel{left:82px;top:1715px;width:1040px;height:1110px;background:var(--panel)}
.tile{width:300px}
.g1{left:135px;top:1865px;height:380px;background:
  radial-gradient(ellipse at 60% 50%,#ddd6c8 0%,rgba(221,214,200,0) 45%),
  radial-gradient(ellipse at 35% 25%,#b6322f 0%,rgba(182,50,47,0) 25%),
  linear-gradient(135deg,#6c4e3a,#a58a73)}
.g2{left:450px;top:1865px;height:380px;display:flex;align-items:center;justify-content:center;background:
  radial-gradient(ellipse at 50% 70%,#8a8586 0%,rgba(138,133,134,0) 50%),
  linear-gradient(135deg,#3a3839,#5a5656)}
.g3{left:765px;top:1865px;height:380px;background:
  radial-gradient(ellipse at 50% 60%,#f4ecea 0%,rgba(244,236,234,0) 45%),
  radial-gradient(circle at 90% 30%,#e2a7a6 0%,rgba(226,167,166,0) 30%),
  linear-gradient(135deg,#e6e6e2,#c9cfc2)}
.g4{left:135px;top:2265px;height:380px;background:
  radial-gradient(ellipse at 45% 65%,#f3efe8 0%,rgba(243,239,232,0) 45%),
  linear-gradient(180deg,#b57b3d 0%,#d8b58a 45%,#f0ede8 100%)}
.g5{left:450px;top:2265px;height:380px;background:
  radial-gradient(ellipse at 45% 60%,#f2f0ee 0%,rgba(242,240,238,0) 45%),
  linear-gradient(135deg,#e3e3e3,#b6b3b5)}
.g6{left:765px;top:2265px;height:380px;background:
  radial-gradient(ellipse at 50% 55%,#aeb8b8 0%,rgba(174,184,184,0) 40%),
  linear-gradient(135deg,#eeece9,#d4ccc6)}

/* contact */
.field{border:1px solid var(--line);background:#fff;font-size:11px;font-style:italic;color:var(--ink);padding:15px 18px}
.f-first{left:260px;top:3005px;width:285px;height:47px}
.f-last{left:260px;top:3065px;width:285px;height:47px}
.f-email{left:260px;top:3125px;width:285px;height:47px}
.f-msg{left:557px;top:3005px;width:403px;height:167px;padding-top:16px}

/* footer */
.footer-panel{left:82px;top:3325px;width:1040px;height:350px;background:var(--panel)}
.foot-brand{left:132px;top:3378px;font-size:22px;color:var(--ink)}
.foot-brand::before{content:"";display:inline-block;width:11px;height:11px;border:2px solid var(--gold);border-radius:50%;margin-right:7px;vertical-align:middle}
.foot-about{left:134px;top:3443px;width:180px;font-size:11px;line-height:15px;color:var(--text)}
.foot-more{left:134px;top:3505px;font-size:11px;font-style:italic;color:var(--ink);border-bottom:1px solid var(--ink)}
.socials{left:134px;top:3545px;display:flex;gap:9px}
.socials span{width:13px;height:13px;background:var(--ink);border-radius:3px}
.foot-head{top:3392px;font-size:17px;font-weight:400;color:var(--ink);letter-spacing:.5px}
.foot-list{top:3440px;font-size:11px;line-height:17px;list-style:disc;padding-left:14px;color:var(--text)}
.contact-list{left:752px;top:3432px;font-size:11px;line-height:16px;color:var(--text)}
.contact-list div{display:flex;align-items:flex-start;gap:6px}
.contact-list svg{flex:none;margin-top:3px}
.news-field{left:930px;top:3447px;width:150px;height:32px;border:1px solid var(--line);background:#fff;font-size:9px;font-style:italic;padding:10px 6px;color:var(--ink)}
.news-btn{left:930px;top:3482px;width:150px;height:32px;font-size:9px}
.foot-rule{left:132px;top:3592px;width:951px;height:2px;background:linear-gradient(90deg,var(--ink),var(--gold) 50%,var(--ink))}
.copyright{left:132px;top:3614px;font-size:10px;color:var(--ink)}
.legal{right:118px;top:3614px;font-size:10px;color:var(--ink)}
</style>
</head>
<body>

<header>
  <div class="abs menu-toggle">MENU<span class="l1"></span><span class="l2"></span></div>
  <div class="abs brand">Velora Studio</div>
  <a class="abs book-link">Book Your Shoot</a>
  <nav class="abs main-nav">
    <span class="active">HOME</span><span>SERVICES</span><span>GALLERYS</span><span>BLOG</span><span>ABOUT</span><span>CONTACT</span>
  </nav>
</header>

<section>
  <div class="abs hero-photo photo" role="img" aria-label="Woman in a light blue top lying on floral bed linen"></div>
  <div class="abs hero-pre">WE CAPTURE YOUR</div>
  <div class="abs hero-big">Beautiful</div>
  <div class="abs hero-post">MEMORIES</div>
</section>

<section>
  <div class="abs about-panel"></div>
  <h2 class="abs section-title script" style="top:722px">About us</h2>
  <p class="abs about-copy" style="top:815px">Lorem Ipsum is simply dummy text of the printing and typesetting industry. Lorem Ipsum has been the industry's standard dummy text ever since the 1500s, when an unknown printer took a galley of type and scrambled it to make a type specimen book.</p>
  <p class="abs about-copy" style="top:882px">It has survived not only five centuries, but also the leap into electronic typesetting, remaining essentially unchanged.</p>
  <div class="abs btn" style="left:527px;top:970px;width:150px;height:42px">READ MORE</div>
</section>

<section>
  <h2 class="abs section-title script" style="top:1145px">Our Services</h2>
  <div class="abs service svc-wedding" role="img" aria-label="Wedding photo: hands forming a heart over a white dress"><span class="label">Wedding</span></div>
  <div class="abs service svc-boudoir" role="img" aria-label="Boudoir photo: woman in a burgundy cardigan"><span class="label">Boudoir</span></div>
  <div class="abs service svc-outdoors" role="img" aria-label="Outdoor photo: woman in a yellow dress in a field"><span class="label">Outdoors</span></div>
</section>

<section>
  <div class="abs gallery-panel"></div>
  <h2 class="abs section-title script" style="top:1752px">Gallery</h2>
  <div class="abs tile photo g1" role="img" aria-label="Woman in a cream sweater lying on a rug"></div>
  <div class="abs tile photo g2" role="img" aria-label="Woman in a white slip dress seated in a dim room">
    <svg width="40" height="40" viewBox="0 0 40 40" fill="none" stroke="#fff" stroke-width="2.5"><circle cx="17" cy="17" r="12"/><line x1="26" y1="26" x2="37" y2="37"/><line x1="11" y1="17" x2="23" y2="17"/><line x1="17" y1="11" x2="17" y2="23"/></svg>
  </div>
  <div class="abs tile photo g3" role="img" aria-label="Expectant mother in white lace among flowers"></div>
  <div class="abs tile photo g4" role="img" aria-label="Woman in a white shirt lying on a wooden bed"></div>
  <div class="abs tile photo g5" role="img" aria-label="Woman in a lace robe seated on a white chair"></div>
  <div class="abs tile photo g6" role="img" aria-label="Woman in a grey sweater seated on a white floor"></div>
  <div class="abs btn" style="left:527px;top:2707px;width:150px;height:43px">VIEW MORE</div>
</section>

<section>
  <h2 class="abs section-title script" style="top:2882px">Contact us</h2>
  <div class="abs field f-first">First Name</div>
  <div class="abs field f-last">Last Name</div>
  <div class="abs field f-email">Email Address</div>
  <div class="abs field f-msg">Your Massage</div>
  <div class="abs btn" style="left:260px;top:3190px;width:150px;height:43px">SEND NOW</div>
</section>

<footer>
  <div class="abs footer-panel"></div>
  <div class="abs foot-brand">Velora Studio</div>
  <p class="abs foot-about">Lorem Ipsum is simply dummy text of the printing and typesetting industry.</p>
  <span class="abs foot-more">VIEW MORE...</span>
  <div class="abs socials" aria-label="Social links"><span></span><span></span><span></span><span></span><span></span><span></span></div>

  <h3 class="abs foot-head" style="left:395px">QUICK LINK</h3>
  <ul class="abs foot-list" style="left:402px"><li>Home</li><li>Services</li><li>Gallery</li><li>Blog</li><li>about</li><li>Contact</li></ul>

  <h3 class="abs foot-head" style="left:572px">USEFUL LNKS</h3>
  <ul class="abs foot-list" style="left:579px"><li>Login</li><li>Register</li><li>Book a shoot</li></ul>

  <h3 class="abs foot-head" style="left:772px">CONTACT</h3>
  <div class="abs contact-list">
    <div><svg width="10" height="10" viewBox="0 0 10 10"><path d="M2 0l2 2-1 1.5a6 6 0 0 0 3.5 3.5L8 6l2 2-1.5 2C4 10 0 6 0 1.5z" fill="#1a1a1a"/></svg>(+012) 555 014 2</div>
    <div><svg width="10" height="10" viewBox="0 0 10 10"><rect x="1" y="1" width="8" height="8" fill="none" stroke="#1a1a1a" stroke-width="1.5"/></svg>(+012) 555 014 2</div>
    <div><svg width="10" height="10" viewBox="0 0 10 10"><rect x="0.5" y="2" width="9" height="6" fill="none" stroke="#1a1a1a"/><path d="M0.5 2l4.5 3.5L9.5 2" fill="none" stroke="#1a1a1a"/></svg>info@velorastudio.ca</div>
    <div><svg width="10" height="12" viewBox="0 0 10 12"><path d="M5 0a4 4 0 0 1 4 4c0 3-4 8-4 8S1 7 1 4a4 4 0 0 1 4-4z" fill="#1a1a1a"/><circle cx="5" cy="4" r="1.5" fill="#fff"/></svg><span>14 Harbour Lane<br>Halifax, NS B3H 1A1</span></div>
  </div>

  <h3 class="abs foot-head" style="left:927px">NEWSLETTER</h3>
  <div class="abs news-field">Email Address</div>
  <div class="abs btn news-btn">SUBSCRIBE</div>

  <div class="abs foot-rule"></div>
  <p class="abs copyright">© Copyright 2018 Velora Studio - All Right Reserved</p>
  <p class="abs legal">Privacy Policy - Terms &amp; Conditions</p>
</footer>

</body>
</html>
```